Lena Hartwell Web

Lena Hartwell is a singer/songwriter that has a presence in the market for over 20 years. She currently has a website, lenahartwell.example that needs a major makeover. IT needs to be reorganized to; 1) make it more user friendly; 2) enable multi-languages including; Spanish, French, Russian, Japanese, Chinese and Portuguese; 3) enable purchases online through a storefront of promotional merchandise and music tracks. She has a logo that needs an update, as well as we currently have a business card open on PixelBazaar for input. Working to re-brand, or refresh her brand.

Lena Hartwell is the next Rosa Delmont! She has 5 platinum records, Lumen Award nominations and tours with Harold Prescott globally and is Nora Vandermeer's key backup singer for 12 years.
Updates

Some common questions have come up.  Here is some further input:

1) Colors - No specific color in mind but probably earth tones.  Although at this point we''re completely open.  Lena likes classical style, Russian, French decor.  Paris architecture. Greek, Italian textures, Goddess like symbols from the Roman Empire, or the symbols and pomp of the British monarchy.  One name on tap for the new CD is "Lanterns Over Quiet Water"
2) Example website - I have not found a new one specifically, but what I don''t like about the existing one is it is not easy to navigate.  Needs to be streamlined and easy to navigate with a storefront for merchandise and music downloads.  
3) On Logo - We''re revamping a "Global" merchandise rollout logo.  We''ve also considered possibly modifying the old english "Hartwell" family crest which signifies royalty, but have not explored that too much.  The hexagon yellow logo on her current website, I was thinking of modifying to gold (brushed - or polished?), then taking the LH lettering using a fountain pen type look there the line thickness flows with pressure on the pen, then make the gold look like a pillow, with the letter making an impression into the gold pillow.  This expands to a high quality pin, blinged up broach with diamonds imbedded for example, Global label identity, tee shirts, label tag on fashion clothing etc etc. 
 4) One thing marketing has asked us to build is a routine video blog to reach out to fans in a personal way.  Short clips of daily activity, travel prep for shows, etc. Possibly a signup/fanpage where people get emails sent back whenever anything new is posted, like a video blog, new pics, new events.  A menu to choose what you get updates on. 

Thanks, Dennis

Target Market(s)

1) Fan base in Europe, Asia, Latin America and North America
2) Movie producers seeking soundtracks
3) Private clients seeking an outstanding performer for corporate events

Industry/Entity Type

Singer

Requirements
Must have
• Better organization into smaller pages. Items critical include: 1) music tracks, 2) ClipStream links, 3) photos & Video, 4) storefront to enable online merchandise purchase 5) a way to illustrate her genre from; gospel, to rock, funk, R&B, country,

```html
<!DOCTYPE html>
<html lang="en">
<head>
<meta charset="utf-8">
<title>Lena Hartwell</title>
<link rel="stylesheet" href="https://fonts.googleapis.com/css2?family=Alfa+Slab+One&family=Bebas+Neue&family=Federo&family=Open+Sans:wght@400;600&display=swap">
<style>
  :root {
    --bg-dark: #1c1c1c;
    --bg-mid: #3a3a3a;
    --panel: #0f0f0f;
    --tile: #161616;
    --card: #2f2f2f;
    --card-line: #5a5a5a;
    --ribbon: #a51d20;
    --ribbon-dark: #6e1012;
    --ribbon-edge: #c42a2d;
    --white: #ffffff;
    --text: #dcdcdc;
    --dot-active: #d3161b;
  }
  html, body { margin: 0; padding: 0; overflow: hidden; }
  body { width: 1200px; height: 825px; background: var(--bg-dark); }
  .page {
    position: relative; width: 1200px; height: 825px; overflow: hidden;
    background: radial-gradient(ellipse 700px 420px at 600px 240px, var(--bg-mid) 0%, #2a2a2a 55%, var(--bg-dark) 100%);
    font-family: "Open Sans", sans-serif;
  }
  .crowd-band {
    position: absolute; left: 0; bottom: 0; width: 1200px; height: 190px;
    background: linear-gradient(to bottom, rgba(0,0,0,0) 0%, rgba(0,0,0,0.75) 45%, #000 100%);
  }
  .social { position: absolute; left: 0; top: 137px; width: 71px; }
  .social a {
    display: flex; align-items: center; justify-content: center;
    width: 71px; height: 63px; margin-bottom: 3px;
    background: var(--tile); color: var(--white); text-decoration: none;
    font-family: "Open Sans", sans-serif; font-weight: 600; font-size: 11px;
  }
  .site-title {
    position: absolute; left: 252px; top: 58px; margin: 0;
    font-family: "Alfa Slab One", serif; font-weight: 400; font-size: 52px;
    color: var(--white); letter-spacing: 0.5px;
    -webkit-text-stroke: 2px #111;
    text-shadow: 3px 3px 0 #000, 0 0 12px rgba(0,0,0,0.8);
  }
  .slider {
    position: absolute; left: 256px; top: 135px; width: 738px; height: 302px;
    background: var(--white); box-shadow: 0 6px 22px rgba(0,0,0,0.7);
  }
  .slide-photo {
    position: absolute; left: 10px; top: 9px; width: 718px; height: 284px;
    background: linear-gradient(100deg, #6b5a48 0%, #a07a52 35%, #3b3433 60%, #b8875a 85%, #8a6846 100%);
  }
  .slider-dots { position: absolute; right: 18px; bottom: 14px; display: flex; gap: 4px; }
  .slider-dots span { width: 12px; height: 12px; border-radius: 50%; background: var(--white); }
  .slider-dots span.is-active { background: var(--dot-active); }
  .feature-figure {
    position: absolute; left: 772px; top: 22px; width: 124px; height: 432px;
    background:
      linear-gradient(to right, rgba(160,30,28,0) 0%, rgba(184,36,32,0.85) 22%, rgba(205,58,44,0.9) 50%, rgba(170,30,26,0.85) 78%, rgba(160,30,28,0) 100%);
    -webkit-mask-image: linear-gradient(to bottom, transparent 0%, #000 14%, #000 90%, transparent 100%);
            mask-image: linear-gradient(to bottom, transparent 0%, #000 14%, #000 90%, transparent 100%);
  }
  .nav-ribbon { position: absolute; left: 185px; top: 460px; width: 880px; height: 55px; }
  .nav {
    position: absolute; left: 237px; top: 462px; width: 773px; height: 43px;
    display: flex; align-items: center; justify-content: space-around;
    padding: 0 14px; box-sizing: border-box;
    font-family: "Federo", sans-serif; font-size: 16px; letter-spacing: 1px;
  }
  .nav a { color: var(--white); text-decoration: none; }
  .content {
    position: absolute; left: 256px; top: 505px; width: 738px; height: 320px;
    background: var(--panel);
  }
  .about { position: absolute; left: 32px; top: 20px; width: 460px; }
  .about h2 {
    margin: 0 0 16px; font-family: "Bebas Neue", sans-serif; font-weight: 400;
    font-size: 40px; line-height: 40px; color: var(--white);
  }
  .about p { margin: 0 0 12.5px; font-size: 9.2px; line-height: 12.5px; color: var(--text); }
  .articles {
    position: absolute; left: 506px; top: 25px; width: 213px; height: 192px;
    background: var(--card); border: 1px solid #3c3c3c; box-sizing: border-box;
  }
  .articles h3 {
    margin: 0; padding: 8px 0 9px 23px; border-bottom: 1px solid var(--card-line);
    font-family: "Bebas Neue", sans-serif; font-weight: 400; font-size: 27px;
    line-height: 28px; color: var(--white);
  }
  .articles ul { list-style: none; margin: 0; padding: 20px 0 0 23px; }
  .articles li { font-size: 9.2px; line-height: 12.5px; color: var(--text); white-space: nowrap; }
</style>
</head>
<body>
<div class="page">
  <div class="crowd-band" role="img" aria-label="Silhouette of a cheering concert crowd with raised hands"></div>

  <nav class="social" aria-label="Social links">
    <a href="#">Linkup</a>
    <a href="#">Chirp</a>
    <a href="#">ClipStream</a>
  </nav>

  <h1 class="site-title">Lena Hartwell</h1>

  <div class="slider">
    <div class="slide-photo" role="img" aria-label="Portrait of the singer in a car with tan leather seats, wearing a fur collar"></div>
    <div class="slider-dots"><span class="is-active"></span><span></span><span></span><span></span></div>
  </div>
  <div class="feature-figure" role="img" aria-label="The singer standing in a long red satin gown, leaning on the slider frame"></div>

  <svg class="nav-ribbon" viewBox="0 0 880 55" aria-hidden="true">
    <polygon points="0,8 75,8 75,50 0,50 18,29" fill="var(--ribbon-dark)"/>
    <polygon points="880,8 805,8 805,50 880,50 862,29" fill="var(--ribbon-dark)"/>
    <polygon points="52,45 75,55 75,45" fill="#3e0809"/>
    <polygon points="828,45 805,55 805,45" fill="#3e0809"/>
    <rect x="52" y="2" width="776" height="43" fill="var(--ribbon)"/>
    <rect x="52" y="2" width="776" height="2" fill="var(--ribbon-edge)"/>
  </svg>
  <nav class="nav" aria-label="Main">
    <a href="#">Home</a>
    <a href="#">Events</a>
    <a href="#">Media</a>
    <a href="#">Pictures</a>
    <a href="#">About</a>
    <a href="#">Online Store</a>
    <a href="#">Contact</a>
  </nav>

  <main class="content">
    <section class="about">
      <h2>About</h2>
      <p>Lena Hartwell displays the vocal prowess, attitude and range of a true ingenue. (Chartline Weekly)</p>
      <p>With a powerfully unique voice and a definitive sound, Lena Hartwell consistently delivers soul stirring performances that captivate audiences around the world. Using her past as a spring board, Lena channels memories into melodies that are proud and strong. Her rich melodic sound and exciting performance style are rooted in the story of a pastor's daughter with a passion for singing good music.</p>
      <p>With Kerbstone Records, Lena began singing for Movie soundtracks and was even featured in the movie Velvet Floor where she portrayed the artist Ivy Sterling and sang “Tap on the Door” for the soundtrack. She performed “Eyes Only On You” with Franco Dale for the closing credits of Hidden Motive. Lena also sang “Back Where We Started” for the movie Full Throttle starring Curt Raymond. Other notable movies that feature Lena's voice include: Desert Saloon and Crossfire Protocol.</p>
      <p>After returning from Europe promoting and shooting the video for “Nothing Without You” by Luca Bellandi and Sean Walters from Tone Theory, she was privileged to have one of her songs selected by Simone Darrow. “I Let Go” was an instant success with Simone and further drove Lena's writing and singing out front.</p>
      <p>In August 2011 Lena recorded the theme song “Velocity” along with 2 other songs for the Limelight Events show “Glide Spectacular”. The theme song was later remixed by DJ Nova Lane and released on</p>
    </section>

    <aside class="articles">
      <h3>See Other Articles</h3>
      <ul>
        <li>Lena Hartwell on SoundHarbor</li>
        <li>Lena Hartwell Band</li>
        <li>Hoop Legends Red Carpet Gala</li>
        <li>Capitol Folklife Festival</li>
        <li>Riverside Summer Pride</li>
        <li>SBU – Keeping The Music Alive – June 20th</li>
      </ul>
    </aside>
  </main>
</div>
</body>
</html>
```